4 x Designs Required

Hi There,
I require 4 x different designs to be made for 4 new brands of mine however they can be quite interchangeable. HR Plinkr and Marketing Plinkr can be similar just with a difference in colour. The same goes for the Bulletin brands. This means there are ultimately two designs that need perfecting.

There must be a click here CTA on the banner somewhere. :-)

I require the banners in 728x90 format and 960x90 please.

Please use strap lines on the banners such as:
Essential Whitepapers for HR Professionals
Essential Whitepapers for Marketing Professionals
Your No.1 Whitepaper Resource

The brand names:
HR Plinkr
Marketing Plinkr
HR Dispatchly
Marketing Dispatchly

Examples attached.

```html
<!DOCTYPE html>
<html lang="en">
<head>
<meta charset="UTF-8">
<title>Banner Design - 1</title>
<link rel="stylesheet" href="https://fonts.googleapis.com/css2?family=Red+Hat+Display:wght@700;800;900&family=Poppins:ital,wght@0,300;0,400;0,600;0,700;1,600&family=Oswald:wght@600&display=swap">
<style>
  :root {
    --sheet-top: #f5c09f;
    --sheet-bottom: #df98cf;
    --ink: #1a1208;
    --white: #ffffff;
    --dispatch-olive: #2a2006;
    --dispatch-orange: #b03c02;
    --dispatch-red: #b0101c;
    --dispatch-plum: #3a0024;
    --cta-red: #e5254a;
    --plinkr-navy: #0b2663;
    --plinkr-deep: #03082a;
    --plinkr-blue: #0a55b5;
    --plinkr-bright: #1470e8;
    --plinkr-cyan: #1ec8ee;
    --silver: #b9bdc8;
  }
  * { margin: 0; padding: 0; box-sizing: border-box; }
  html, body { width: 1200px; height: 655px; overflow: hidden; }
  body {
    position: relative;
    background: linear-gradient(180deg, var(--sheet-top), var(--sheet-bottom));
    font-family: "Poppins", sans-serif;
    color: var(--ink);
  }
  .sheet-title {
    position: absolute; top: 40px; left: 0; width: 100%;
    text-align: center;
    font-family: "Red Hat Display", sans-serif;
    font-weight: 700; font-size: 43px; line-height: 1;
  }
  .sheet-specs {
    position: absolute; top: 94px; left: 0; width: 100%;
    text-align: center;
    font-family: "Red Hat Display", sans-serif;
    font-weight: 700; font-size: 23px; line-height: 1;
  }
  .banner {
    position: absolute; left: 49px; width: 1103px; height: 103px; overflow: hidden;
  }
  /* Dispatchly banner */
  .banner--dispatchly {
    top: 221px;
    background: linear-gradient(90deg, var(--dispatch-olive) 0%, #6a3a05 25%, var(--dispatch-orange) 48%, var(--dispatch-red) 72%, var(--dispatch-plum) 100%);
  }
  .banner--dispatchly .brand-name {
    position: absolute; left: 24px; top: 28px;
    font-weight: 600; font-size: 31px; line-height: 1; color: var(--white);
  }
  .banner--dispatchly .strapline {
    position: absolute; left: 408px; top: 28px;
    font-size: 26px; line-height: 1.2; color: var(--white); white-space: nowrap;
  }
  .strapline .accent-condensed {
    font-family: "Oswald", sans-serif; font-weight: 600; font-size: 31px;
    letter-spacing: -0.3px;
  }
  .cta-tab {
    position: absolute; right: 0; bottom: 0; width: 112px; height: 27px;
    background: var(--cta-red);
    clip-path: polygon(10px 0, 100% 0, 100% 100%, 0 100%);
    color: var(--white); font-weight: 600; font-style: italic; font-size: 16px;
    line-height: 27px; text-align: right; padding-right: 6px;
  }
  /* Plinkr banner */
  .banner--plinkr { top: 414px; background: linear-gradient(90deg, var(--plinkr-navy), #0a2a6e 70%, #0e3b86); }
  .banner--plinkr .shapes { position: absolute; inset: 0; }
  .banner--plinkr .brand-name {
    position: absolute; left: 16px; top: 40px;
    font-weight: 400; font-size: 33px; line-height: 1; color: var(--white);
  }
  .banner--plinkr .strapline {
    position: absolute; left: 443px; top: 33px;
    font-size: 22.5px; line-height: 1.2; color: var(--white); white-space: nowrap;
  }
  .strapline .accent-bold { color: var(--plinkr-cyan); font-weight: 700; }
  .strapline .light { font-weight: 300; }
  .cta-shield {
    position: absolute; left: 976px; top: 0; width: 116px; height: 88px;
  }
  .cta-shield .cta-text {
    position: absolute; inset: 10px 0 0 0; text-align: center;
    font-family: "Red Hat Display", sans-serif; font-weight: 900;
    color: var(--white); line-height: 0.95;
  }
  .cta-text .small { display: block; font-size: 21px; }
  .cta-text .large { display: block; font-size: 26px; }
</style>
</head>
<body>
  <h1 class="sheet-title">Banner Design - 1</h1>
  <p class="sheet-specs">Size: 960px X 90px &nbsp;| &nbsp; HD Quality &nbsp;| &nbsp;Web &amp; Print both file available</p>

  <section class="banner banner--dispatchly">
    <span class="brand-name">marketing Dispatchly</span>
    <p class="strapline">Essential <span class="accent-condensed">WHITEPAPERS</span> for &nbsp;Marketing Professionals</p>
    <a class="cta-tab">Click Here</a>
  </section>

  <section class="banner banner--plinkr">
    <svg class="shapes" width="1103" height="103" viewBox="0 0 1103 103">
      <defs>
        <linearGradient id="topBand" x1="0" x2="1">
          <stop offset="0" stop-color="#0a2a6e"/>
          <stop offset="0.5" stop-color="var(--plinkr-bright)"/>
          <stop offset="1" stop-color="var(--plinkr-cyan)"/>
        </linearGradient>
        <linearGradient id="silverLine" x1="0" x2="1">
          <stop offset="0" stop-color="#7c818e"/>
          <stop offset="0.6" stop-color="var(--silver)"/>
          <stop offset="1" stop-color="#ffffff"/>
        </linearGradient>
      </defs>
      <rect x="440" y="0" width="663" height="6" fill="url(#topBand)"/>
      <rect x="700" y="35" width="403" height="10" fill="#0d4a90" opacity="0.5"/>
      <polygon class="brand-panel" points="0,0 449,0 368,103 0,103" fill="var(--plinkr-blue)"/>
      <polygon class="top-strip" points="0,0 344,0 323,24 0,24" fill="var(--plinkr-deep)"/>
      <polyline points="0,25 326,25 347,0" fill="none" stroke="url(#silverLine)" stroke-width="4"/>
      <line x1="449" y1="0" x2="368" y2="103" stroke="var(--white)" stroke-width="5"/>
      <rect x="0" y="98" width="370" height="5" fill="url(#silverLine)"/>
    </svg>
    <span class="brand-name">marketing Plinkr</span>
    <p class="strapline"><span class="accent-bold">Essential</span> <span class="light">Whitepapers</span> <span class="accent-bold">for HR Professionals</span></p>
    <a class="cta-shield">
      <svg width="116" height="88" viewBox="0 0 116 88">
        <polygon points="3,0 113,0 113,62 58,86 3,62" fill="var(--plinkr-deep)" stroke="var(--white)" stroke-width="5"/>
      </svg>
      <span class="cta-text"><span class="small">CLICK</span><span class="large">HERE</span></span>
    </a>
  </section>
</body>
</html>
```